Granite Ridge Holdings

I have a real estate investment business.

** I need editable vector files of the final design.

Industry/Entity Type

Real Estate

Contact Information for Business Card

I would like the card to be clear and direct with the company name and contact info. I would prefer not to have a design that is too busy (i.e., with excessive detail) in the business card.

Font styles to use
Sans Serif

Requirements
Must have
• My card must have the following information listed below:
• Company name: Grainite Ridge Holdings LLC
• My name: Daniel Vorsley
• Phone number: (555) 218-9067
• Email address: dtvorsley@mailbox-example.net
• Keywords: “Real Estate Investments”
Nice to have
• I would like to have a design that resembles the characteristics/uses of obsidian stone which resembles something related to strength and resilience. Perhaps something with sharp, sleek color transitions as well.

```html
<!DOCTYPE html>
<html lang="en">
<head>
<meta charset="utf-8">
<title>Grainite Ridge Holdings LLC – Business Card</title>
<link rel="stylesheet" href="https://fonts.googleapis.com/css2?family=Inter:ital,wght@0,300;0,400;1,300&display=swap">
<style>
  :root {
    --page-bg: #e9e9e7;
    --card-bg: #050505;
    --ink: #f2f2f2;
    --ink-soft: #d6d6d6;
    --stone-dark: #0b0b0b;
    --stone-mid: #3a3a3a;
    --stone-light: #8a8a8a;
  }
  * { margin: 0; padding: 0; box-sizing: border-box; }
  html, body {
    width: 1154px;
    height: 1200px;
    overflow: hidden;
    background: var(--page-bg);
    font-family: "Inter", sans-serif;
  }
  .canvas {
    width: 1154px;
    height: 1200px;
    display: flex;
    align-items: center;
    justify-content: center;
  }
  .business-card {
    position: relative;
    width: 630px;
    height: 1100px;
    background: var(--card-bg);
    border-radius: 26px;
    overflow: hidden;
    color: var(--ink);
  }
  .brand {
    position: absolute;
    top: 62px;
    left: 70px;
    right: 40px;
  }
  .brand-name {
    display: flex;
    align-items: center;
    gap: 12px;
    font-weight: 300;
    font-size: 33px;
    letter-spacing: 0.2px;
    color: var(--ink);
    white-space: nowrap;
  }
  .brand-square {
    width: 14px;
    height: 14px;
    background: var(--ink);
    flex: none;
  }
  .tagline {
    margin-top: 8px;
    font-style: italic;
    font-weight: 300;
    font-size: 25px;
    color: var(--ink);
  }
  .contact {
    position: absolute;
    top: 548px;
    left: 60px;
  }
  .person-name {
    font-weight: 400;
    font-size: 30px;
    color: var(--ink);
    margin-bottom: 18px;
  }
  .contact-line {
    font-weight: 300;
    font-size: 22px;
    color: var(--ink-soft);
    line-height: 1.45;
  }
  .stone-photo {
    position: absolute;
    left: 0;
    right: 0;
    bottom: 0;
    height: 440px;
    background:
      linear-gradient(170deg, var(--card-bg) 0%, var(--card-bg) 14%, var(--stone-mid) 30%, var(--stone-dark) 55%, var(--stone-mid) 78%, var(--stone-light) 100%);
    clip-path: polygon(0 18%, 35% 11%, 72% 8%, 100% 3%, 100% 100%, 0 100%);
  }
</style>
</head>
<body>
  <main class="canvas">
    <article class="business-card">
      <header class="brand">
        <div class="brand-name"><span>Grainite Ridge Holdings LLC</span><span class="brand-square"></span></div>
        <p class="tagline">Real Estate Investments</p>
      </header>

      <section class="contact">
        <h1 class="person-name">Daniel Vorsley</h1>
        <p class="contact-line">(555) 218-9067</p>
        <p class="contact-line">dtvorsley@mailbox-example.net</p>
      </section>

      <div class="stone-photo" role="img" aria-label="Close-up photograph of dark, rugged obsidian stone ridges lit softly from the side"></div>
    </article>
  </main>
</body>
</html>
```